Brightmoor Notes To Do List

I am looking to design a new "Study To Do List" for High School students (Ages 15 - 18) . This will be printed as an A4 notepad and so should only be a single A4 page.

The Design will need to be professional and look semi-serious but also be appealing to High school students (Ages 15 - 18) and should NOT be gender specific.

I have attached a word document outlining the structure of the page. The space provided should be large enough that people can write in it comfortably.

The notepad will most likely be printed in black and white but I'm also looking at coloured options - colours should be kept to a minimum.

This will be printed professionally and should also include a 3mm bleed.

The design should also include the business logo (included in the word document)

Target Market(s)

High School students (Ages 15 - 18). Both genders

Industry/Entity Type

Education

Font styles to use
Serif
Sans Serif

Requirements
Must have
• Please see the word document attached.
Should not have
• Too much colour

```html
<!DOCTYPE html>
<html lang="en">
<head>
<meta charset="utf-8">
<title>Brightmoor Notes – Study To Do List</title>
<link href="https://fonts.googleapis.com/css2?family=Source+Sans+3:wght@400;600;700&display=swap" rel="stylesheet">
<style>
  :root {
    --backdrop: #ececec;
    --paper: #ffffff;
    --ink: #4a4a4a;
    --ink-dark: #3c3c3c;
    --rule: #8a8a8a;
    --dots: #9a9a9a;
    --band: #555555;
    --band-text: #ffffff;
  }
  * { box-sizing: border-box; margin: 0; padding: 0; }
  html, body {
    width: 1200px; height: 1200px; overflow: hidden;
    background: var(--backdrop);
    font-family: "Source Sans 3", sans-serif;
    color: var(--ink);
  }
  .sheet {
    position: absolute; left: 176px; top: 0;
    width: 848px; height: 1200px;
    background: var(--paper);
  }
  .abs { position: absolute; }

  .date { left: 50px; top: 46px; font-size: 16px; font-weight: 700; display: flex; align-items: flex-end; }
  .date .fill { width: 154px; margin-left: 8px; border-bottom: 1px dashed var(--dots); margin-bottom: 4px; }

  .brand { left: 640px; top: 70px; display: flex; align-items: center; gap: 8px; }
  .brand .dot { width: 22px; height: 22px; border-radius: 50%; background: var(--ink-dark); }
  .brand .name { font-size: 24px; font-weight: 700; color: var(--ink-dark); }

  .section-title { font-size: 17px; font-weight: 700; letter-spacing: 0.3px; color: var(--ink-dark); }
  .section-icon { width: 40px; height: 40px; }

  .grid { left: 76px; width: 719px; }
  .grid .row { position: absolute; left: 0; width: 100%; height: 25.6px; font-size: 15px; }
  .grid .row.ruled { border-bottom: 1px solid var(--rule); }
  .grid .num { position: absolute; top: 2px; }
  .grid .split { position: absolute; top: 0; bottom: 0; width: 1px; background: var(--rule); }

  .line-row { position: absolute; left: 80px; width: 715px; height: 22px; display: flex; align-items: flex-end; font-size: 16px; }
  .line-row .label { white-space: nowrap; }
  .line-row .label.strong { font-weight: 700; }
  .line-row .fill { flex: 1; border-bottom: 1px dashed var(--dots); margin: 0 0 4px 6px; }
  .line-row.task { left: 90px; width: 705px; }
  .line-row.task .fill { margin-left: 26px; }
  .line-row.assess { left: 86px; width: 709px; }
  .line-row .due { margin-left: 8px; }

  .band { left: 76px; top: 1052px; width: 719px; height: 27px; background: var(--band); color: var(--band-text); font-size: 16px; font-weight: 700; display: flex; }
  .band .cell { display: flex; align-items: center; justify-content: center; gap: 6px; }
  .band .note-head { width: 328px; border-right: 1px solid var(--paper); }
  .band .practice-head { flex: 1; }
</style>
</head>
<body>
<main class="sheet">

  <div class="abs date">Date: <span class="fill"></span></div>

  <div class="abs brand"><span class="dot"></span><span class="name">Brightmoor Notes</span></div>

  <!-- Revision -->
  <svg class="abs section-icon" style="left:36px;top:106px" viewBox="0 0 40 40" aria-hidden="true">
    <path d="M32 22a13 13 0 1 1-6-11" fill="none" stroke="#555" stroke-width="3"/>
    <path d="M14 27l3-8 12-12 5 5-12 12z" fill="#555"/>
  </svg>
  <div class="abs section-title" style="left:91px;top:118px">REVISION</div>
  <div class="abs grid" style="top:145px;height:95px">
    <div class="split" style="left:359px"></div>
    <div class="row ruled" style="top:0"><span class="num" style="left:9px">1</span><span class="num" style="left:370px">5</span></div>
    <div class="row ruled" style="top:25.6px"><span class="num" style="left:9px">2</span><span class="num" style="left:370px">6</span></div>
    <div class="row ruled" style="top:51.2px"><span class="num" style="left:9px">3</span><span class="num" style="left:370px">7</span></div>
    <div class="row" style="top:76.8px"><span class="num" style="left:9px">4</span><span class="num" style="left:370px">8</span></div>
  </div>

  <!-- Homework -->
  <svg class="abs section-icon" style="left:42px;top:252px" viewBox="0 0 40 40" aria-hidden="true">
    <circle cx="20" cy="20" r="18" fill="none" stroke="#555" stroke-width="3"/>
    <rect x="10" y="11" width="9" height="19" fill="#555"/>
    <path d="M22 13h9M22 18h9M22 23h9M22 28h9" stroke="#555" stroke-width="2"/>
  </svg>
  <div class="abs section-title" style="left:91px;top:263px">HOMEWORK</div>

  <div class="line-row" style="top:284px"><span class="label strong">Subject:</span><span class="fill"></span></div>
  <div class="line-row task" style="top:314px"><span class="label">Task:</span><span class="fill"></span></div>
  <div class="line-row" style="top:344px"><span class="label strong">Subject:</span><span class="fill"></span></div>
  <div class="line-row task" style="top:374px"><span class="label">Task:</span><span class="fill"></span></div>
  <div class="line-row" style="top:404px"><span class="label strong">Subject:</span><span class="fill"></span></div>
  <div class="line-row task" style="top:434px"><span class="label">Task:</span><span class="fill"></span></div>
  <div class="line-row" style="top:464px"><span class="label strong">Subject:</span><span class="fill"></span></div>
  <div class="line-row task" style="top:494px"><span class="label">Task:</span><span class="fill"></span></div>
  <div class="line-row" style="top:524px"><span class="label strong">Subject:</span><span class="fill"></span></div>
  <div class="line-row task" style="top:554px"><span class="label">Task:</span><span class="fill"></span></div>
  <div class="line-row" style="top:584px"><span class="label strong">Subject:</span><span class="fill"></span></div>
  <div class="line-row task" style="top:614px"><span class="label">Task:</span><span class="fill"></span></div>

  <!-- Assessments -->
  <svg class="abs section-icon" style="left:46px;top:648px" viewBox="0 0 40 40" aria-hidden="true">
    <path d="M8 8h6M26 8h4v8M30 30v6H8V8" fill="none" stroke="#555" stroke-width="3"/>
    <rect x="14" y="4" width="12" height="7" rx="2" fill="none" stroke="#555" stroke-width="3"/>
    <path d="M16 30l2-7 14-14 5 5-14 14z" fill="#555"/>
  </svg>
  <div class="abs section-title" style="left:91px;top:659px">ASSESSMENTS</div>

  <div class="line-row assess" style="top:681px"><span class="label strong">Assessment:</span><span class="fill" style="flex:0 0 246px;margin-left:2px"></span><span class="label due">Due</span><span class="fill"></span></div>
  <div class="line-row assess" style="top:711px"><span class="label">Element:</span><span class="fill"></span></div>
  <div class="line-row assess" style="top:741px"><span class="label strong">Assessment:</span><span class="fill" style="flex:0 0 246px;margin-left:2px"></span><span class="label due">Due</span><span class="fill"></span></div>
  <div class="line-row assess" style="top:771px"><span class="label">Element:</span><span class="fill"></span></div>
  <div class="line-row assess" style="top:801px"><span class="label strong">Assessment:</span><span class="fill" style="flex:0 0 246px;margin-left:2px"></span><span class="label due">Due</span><span class="fill"></span></div>
  <div class="line-row assess" style="top:831px"><span class="label">Element:</span><span class="fill"></span></div>
  <div class="line-row assess" style="top:861px"><span class="label strong">Assessment:</span><span class="fill" style="flex:0 0 246px;margin-left:2px"></span><span class="label due">Due</span><span class="fill"></span></div>
  <div class="line-row assess" style="top:891px"><span class="label">Element:</span><span class="fill"></span></div>
  <div class="line-row assess" style="top:921px"><span class="label strong">Assessment:</span><span class="fill" style="flex:0 0 246px;margin-left:2px"></span><span class="label due">Due</span><span class="fill"></span></div>
  <div class="line-row assess" style="top:951px"><span class="label">Element:</span><span class="fill"></span></div>
  <div class="line-row assess" style="top:981px"><span class="label strong">Assessment:</span><span class="fill" style="flex:0 0 246px;margin-left:2px"></span><span class="label due">Due</span><span class="fill"></span></div>
  <div class="line-row assess" style="top:1011px"><span class="label">Element:</span><span class="fill"></span></div>

  <!-- Note / Practice -->
  <div class="abs band">
    <div class="cell note-head">
      <svg width="22" height="20" viewBox="0 0 22 20" aria-hidden="true"><path d="M2 3h16l2 15H4z" fill="none" stroke="#fff" stroke-width="1.8"/><path d="M10 1v6" stroke="#fff" stroke-width="1.8"/></svg>
      NOTE
    </div>
    <div class="cell practice-head">
      <svg width="20" height="20" viewBox="0 0 20 20" aria-hidden="true"><rect x="0" y="0" width="20" height="20" rx="3" fill="#fff"/><circle cx="7" cy="12" r="4" fill="none" stroke="#555" stroke-width="2.4" stroke-dasharray="2 1.5"/><circle cx="14" cy="6" r="3" fill="none" stroke="#555" stroke-width="2" stroke-dasharray="1.6 1.2"/></svg>
      PRACTICE
    </div>
  </div>
  <div class="abs grid" style="top:1079px;height:99px">
    <div class="split" style="left:161px"></div>
    <div class="split" style="left:328px"></div>
    <div class="row ruled" style="top:0"><span class="num" style="left:9px">1</span><span class="num" style="left:171px">5</span></div>
    <div class="row ruled" style="top:25.6px"><span class="num" style="left:9px">2</span><span class="num" style="left:171px">6</span></div>
    <div class="row ruled" style="top:51.2px"><span class="num" style="left:9px">3</span><span class="num" style="left:171px">7</span></div>
    <div class="row" style="top:76.8px"><span class="num" style="left:9px">4</span><span class="num" style="left:171px">8</span></div>
  </div>

</main>
</body>
</html>
```